Summit Glossfloor & Honing
I'm looking for a business card and logo design for my
new Polished Concrete & Grinding business,
If you were to look up Summit in the dictionary it would
say, first in importance, order, or position; leading.
Polished Concrete floors are a niche market, that are being used currently in Shopping centres, office spaces and by most high end architects, builders and designers.
i need my business card & logo to stand out from my
competitors, i need my design + logo to reflect this it
needs to be simple, professional, eye catching, easy
to read and scream quality. The logo will need to be
suitable for a whole range of applications including,
uniforms, letter heads, stickers, and eventually
incorporating in vehicle vinyl wrapping.
Target Market(s)
Builders, architects, Interior designers & home owners
Contact Information for Business Card
Front side:
- Summit Glossfloor & Honing.
- Logo
Rear side:
- Liam Varga
- 0491735082
- info@summitgfh.com.au
- commercial - domestic - industrial
- (later down the line website & space for
social media links
www.summitglossfloor.com.au)
Colors
Designer to choose colors to be used in the design.
Look and feel

```html
<!DOCTYPE html>
<html lang="en">
<head>
<meta charset="utf-8">
<title>Summit Glossfloor &amp; Honing – Business Card</title>
<link href="https://fonts.googleapis.com/css2?family=IBM+Plex+Sans:wght@400;600;700&display=swap" rel="stylesheet">
<style>
  :root {
    --backdrop: #2b2e33;
    --card: #0b0b0b;
    --cream: #efe5d6;
    --cream-soft: #d9cfc1;
    --divider: #5a5650;
  }
  * { box-sizing: border-box; margin: 0; padding: 0; }
  html, body {
    width: 1200px; height: 900px; overflow: hidden;
    background: var(--backdrop);
    font-family: "IBM Plex Sans", Arial, sans-serif;
    color: var(--cream);
  }
  .canvas {
    position: relative; width: 1200px; height: 900px;
    display: flex; flex-direction: column; align-items: center; justify-content: center; gap: 50px;
  }
  .card {
    position: relative; width: 560px; height: 320px;
    background: var(--card);
    box-shadow: 0 14px 30px rgba(0,0,0,.45);
  }
  .card-frame {
    position: absolute; inset: 16px;
    border: 1.5px solid var(--cream);
  }

  /* Front */
  .front-brand {
    position: absolute; inset: 0;
    display: flex; flex-direction: column; align-items: center; justify-content: center; gap: 14px;
  }
  .brand-square {
    width: 64px; height: 64px; background: var(--cream);
  }
  .brand-name {
    font-weight: 700; text-transform: uppercase; letter-spacing: .08em;
    color: var(--cream); text-align: center; line-height: 1.25;
  }
  .front-brand .brand-name { font-size: 22px; }

  /* Back */
  .back-brand {
    position: absolute; left: 44px; top: 52px; width: 170px;
    display: flex; flex-direction: column; align-items: center; gap: 10px;
  }
  .back-brand .brand-square { width: 40px; height: 40px; }
  .back-brand .brand-name { font-size: 12px; }
  .back-divider {
    position: absolute; left: 0; top: 0; width: 560px; height: 320px; pointer-events: none;
  }
  .social {
    position: absolute; left: 62px; bottom: 52px;
    display: flex; align-items: center; gap: 8px;
    font-size: 13px; color: var(--cream-soft);
  }
  .social-dot { width: 12px; height: 12px; border-radius: 50%; background: var(--cream-soft); }

  .contact-block {
    position: absolute; left: 262px; top: 62px; right: 36px;
  }
  .person-name { font-size: 24px; font-weight: 700; letter-spacing: .02em; }
  .service-line { margin-top: 6px; font-size: 13.5px; color: var(--cream-soft); letter-spacing: .02em; }
  .contact-list { list-style: none; margin-top: 30px; display: flex; flex-direction: column; gap: 10px; }
  .contact-item {
    display: flex; align-items: center; gap: 10px;
    font-size: 13.5px; color: var(--cream-soft); letter-spacing: .03em;
  }
  .contact-icon { width: 14px; height: 14px; flex: none; }
  .contact-at { width: 14px; text-align: center; font-weight: 600; font-size: 14px; color: var(--cream); }
</style>
</head>
<body>
<main class="canvas">

  <section class="card card-front" aria-label="Card front">
    <div class="card-frame"></div>
    <div class="front-brand">
      <span class="brand-square"></span>
      <p class="brand-name">Summit Glossfloor<br>&amp; Honing</p>
    </div>
  </section>

  <section class="card card-back" aria-label="Card back">
    <div class="card-frame"></div>
    <svg class="back-divider" viewBox="0 0 560 320" aria-hidden="true">
      <line x1="238" y1="70" x2="210" y2="200" stroke="var(--divider)" stroke-width="1.5"/>
    </svg>

    <div class="back-brand">
      <span class="brand-square"></span>
      <p class="brand-name">Summit Glossfloor<br>&amp; Honing</p>
    </div>

    <div class="contact-block">
      <h1 class="person-name">Liam Varga</h1>
      <p class="service-line">commercial - domestic - industrial</p>
      <ul class="contact-list">
        <li class="contact-item">
          <svg class="contact-icon" viewBox="0 0 24 24" aria-hidden="true"><path fill="var(--cream)" d="M6.6 10.8a15.1 15.1 0 0 0 6.6 6.6l2.2-2.2a1 1 0 0 1 1-.25 11.4 11.4 0 0 0 3.6.57 1 1 0 0 1 1 1V20a1 1 0 0 1-1 1A17 17 0 0 1 3 4a1 1 0 0 1 1-1h3.5a1 1 0 0 1 1 1c0 1.25.2 2.45.57 3.57a1 1 0 0 1-.25 1z"/></svg>
          <span>0491735082</span>
        </li>
        <li class="contact-item">
          <span class="contact-at">@</span>
          <span>info@summitgfh.com.au</span>
        </li>
        <li class="contact-item">
          <svg class="contact-icon" viewBox="0 0 24 24" aria-hidden="true"><circle cx="12" cy="12" r="9" fill="none" stroke="var(--cream)" stroke-width="2"/><path d="M3 12h18M12 3c3 3.5 3 14.5 0 18M12 3c-3 3.5-3 14.5 0 18" fill="none" stroke="var(--cream)" stroke-width="1.6"/></svg>
          <span>www.summitglossfloor.com.au</span>
        </li>
      </ul>
    </div>

    <div class="social">
      <span class="social-dot"></span>
      <span>@summitgfh</span>
    </div>
  </section>

</main>
</body>
</html>
```